Business Card Design Project

I want my business cards to stand and feel timeless! I also want people to get their hands on them and freak out over how cool these are, I already have a logo i just want a very cool card design! this is for a makeup artist and maybe one day a line of cosmetics.

Target Market(s)

I want this to target women from 18 to 45

Industry/Entity Type

Business

Font styles to use
Decorative
Script

Colors

Designer to choose colors to be used in the design.

Requirements
Must have
• it must be elegante

```html
<!DOCTYPE html>
<html lang="en">
<head>
<meta charset="utf-8">
<title>Mara Lise — Business Card</title>
<link rel="stylesheet" href="https://fonts.googleapis.com/css2?family=Tenor+Sans&family=Josefin+Sans:wght@300&display=swap">
<style>
  :root {
    --canvas: #ffffff;
    --card: #000000;
    --accent: #e8185f;
    --ink-light: #ffffff;
  }
  html, body {
    margin: 0;
    padding: 0;
    width: 1200px;
    height: 1000px;
    overflow: hidden;
    background: var(--canvas);
  }
  .canvas {
    position: relative;
    width: 1200px;
    height: 1000px;
  }
  .card {
    position: absolute;
    left: 292px;
    width: 615px;
    height: 200px;
    background: var(--card);
  }
  .card--front { top: 281px; }
  .card--back { top: 519px; height: 199px; }

  .brand-name {
    position: absolute;
    left: 0;
    right: 0;
    top: 52px;
    margin: 0;
    text-align: center;
    font-family: "Josefin Sans", sans-serif;
    font-weight: 300;
    font-size: 60px;
    line-height: 1;
    letter-spacing: 4px;
    color: var(--accent);
    text-transform: uppercase;
  }

  .small-caps {
    font-family: "Tenor Sans", sans-serif;
    font-variant: small-caps;
    position: absolute;
    margin: 0;
    white-space: nowrap;
    line-height: 1;
  }
  .person-name {
    left: 80px;
    top: 53px;
    font-size: 16px;
    letter-spacing: 3px;
    color: var(--accent);
  }
  .person-role {
    left: 80px;
    top: 74px;
    font-size: 11px;
    letter-spacing: 2.5px;
    color: var(--ink-light);
    text-transform: uppercase;
  }
  .contact {
    position: absolute;
    right: 37px;
    top: 120px;
    display: flex;
    align-items: center;
    gap: 16px;
    font-family: "Tenor Sans", sans-serif;
    font-size: 11px;
    letter-spacing: 3px;
    color: var(--accent);
    line-height: 1;
  }
  .contact__divider {
    width: 1px;
    height: 17px;
    background: var(--accent);
  }
  .tagline {
    right: 31px;
    top: 152px;
    text-align: right;
    font-size: 10px;
    letter-spacing: 2px;
    line-height: 13px;
    color: var(--ink-light);
  }
</style>
</head>
<body>
<main class="canvas">
  <section class="card card--front" aria-label="Card front">
    <h1 class="brand-name">Mara Lise</h1>
  </section>

  <section class="card card--back" aria-label="Card back">
    <p class="small-caps person-name">Mara Lise</p>
    <p class="small-caps person-role">Makeup Artist</p>
    <div class="contact">
      <span class="contact__email">mara@mlmakeup.com</span>
      <span class="contact__divider" aria-hidden="true"></span>
      <span class="contact__web">www.mlmakeup.com</span>
    </div>
    <p class="small-caps tagline">Lorem ipsum sit marter amet,<br>cons adipisciing dolr in elit.</p>
  </section>
</main>
</body>
</html>
```